General Contractor Website Design

We are working with a General Contractor in California that specializes in building custom kitchens, baths, and homes for high-end clients.

Here are some websites for inspiration:
https://mervalstudio.com/
https://ridgelorebuilders.com
https://www.framplank.com
https://www.quellnest.com
https://www.zelhaus.com
https://plyestates.com

Thank you for taking the time to consider designing a website for us. We are web developers based in Stockton, CA, USA. Most of our projects go through the same process. Understanding this process may help you win a project with us. We custom-code all of our websites in-house. We don’t have any requirements as to what tools you use for your design, but we ask that you follow these guidelines.

IMAGES:
If you use any images or icons in the design, we ask that you have a link to the asset so we can purchase the image/icon. Most of the designs we submit do not have the customer’s images on them unless they have some great images. Be creative; show us the feeling you are trying to portray with your image choices. Use any royalty-free site you choose. We subscribe to Vantrix and mainly use their images, but we can purchase images outside of Vantrix. PLEASE NOTE: we will not submit designs to clients with watermarks on the images.

FONTS:
We ask that you identify the fonts you’re using in the design. This can be done in a message if you want. We typically use Orlimo Fonts and Vantrix Fonts.

CONTENT:
We're always open to different content and ideas. We often submit designs with stock images so the client can see our vision. We typically take pictures after the website launch to use their images with our vision. Lorem Ipsum is fine for paragraphs, but we ask that you make the Headers with correct English. We want to be able to show the vision and identify the sections of the website.

INSPIRATION:
We typically add a couple of links in the brief of websites we like to help you get started in your design.

REVISIONS:
We do not often ask for revisions of the designs unless we see something in the design that may not appeal to the client. If there are slight changes that we want to make, we do that in the development process.

FEEDBACK:
We rarely give feedback on designs during the design process. We are working on many website projects and do not have the time to provide feedback. We usually respond if your request is well thought out and asks specific questions, but a note asking “feedback, please” usually goes unanswered.

```html
<!DOCTYPE html>
<html lang="en">
<head>
<meta charset="utf-8">
<title>Vellmark Builders</title>
<link href="https://fonts.googleapis.com/css2?family=Poppins:wght@300;400;500;600;700&display=swap" rel="stylesheet">
<style>
:root{
  --red:#e5353b;
  --red-deep:#c9313a;
  --ink:#111111;
  --text:#5c5c5c;
  --gray:#e7e7e7;
  --white:#ffffff;
  --black:#000000;
}
*{margin:0;padding:0;box-sizing:border-box}
html,body{width:1200px;height:4570px;overflow:hidden}
body{position:relative;font-family:'Poppins',sans-serif;color:var(--ink);background:var(--white)}
.abs{position:absolute}
a{text-decoration:none;color:inherit}

/* header */
.brand{position:absolute;display:flex;align-items:center;gap:12px;font-family:'Poppins',sans-serif;font-weight:600;color:var(--red);letter-spacing:4px;text-transform:uppercase}
.brand .mark{width:26px;height:26px;background:var(--red)}
.site-header .brand{left:85px;top:42px;font-size:22px}
.main-nav{position:absolute;right:85px;top:52px;display:flex;gap:38px;font-size:15px;color:#333}
.main-nav .active{color:var(--red)}

/* hero */
.hero{position:absolute;left:0;top:123px;width:1200px;height:552px}
.hero-photo{position:absolute;inset:0;background:linear-gradient(160deg,#9aa4b8 0%,#6f7890 35%,#4d5165 55%,#8a6d55 80%,#3d4a2f 100%)}
.hero h1{position:absolute;left:85px;top:130px;font-size:39px;line-height:52px;font-weight:600;color:var(--ink);width:640px}
.hero p{position:absolute;left:85px;top:250px;width:450px;font-size:15px;line-height:26px;color:#222}
.btn{display:inline-flex;align-items:center;justify-content:center;background:var(--red);color:var(--white);font-weight:500}
.hero .btn{position:absolute;left:85px;top:347px;width:171px;height:63px;font-size:21px}
.scroll-cue{position:absolute;left:580px;top:532px;width:40px;height:40px;border-radius:50%;background:var(--white);box-shadow:0 2px 6px rgba(0,0,0,.25)}

/* about */
.about-block{left:0;top:800px;width:325px;height:471px;background:var(--red-deep)}
.about-frame{left:325px;top:838px;width:332px;height:374px;border:2px solid var(--red-deep);border-left:none}
.about-img{left:137px;top:861px;width:491px;height:350px;background:linear-gradient(120deg,#f2f2f0,#c9ccd0 45%,#8f9398 70%,#e8e6e2)}
.section-title{font-weight:700;color:var(--ink);text-transform:uppercase}
.section-title span{color:var(--red)}
.about-title{left:714px;top:822px;font-size:40px}
.about-text{left:714px;top:918px;width:400px;font-size:15.5px;line-height:31px;color:#444}
.about-btn{left:714px;top:1147px;width:158px;height:48px;font-size:16px}

/* services */
.services{left:0;top:1349px;width:1200px;height:1322px;background:var(--gray)}
.center-title{left:0;width:1200px;text-align:center;font-size:40px}
.band{left:0;width:1200px;background:var(--white)}
.red-block{background:var(--red)}
.frame{border:2px solid var(--red-deep)}
.kitchen{background:linear-gradient(180deg,#f4f4f3 0%,#e6e6e4 45%,#b9b4ad 75%,#6a5c4f 100%)}
.service h3{position:absolute;font-size:19px;font-weight:600;color:var(--red);text-transform:uppercase}
.service p{position:absolute;width:450px;font-size:14.5px;line-height:26px;color:var(--text)}
.service .btn{position:absolute;width:117px;height:43px;font-size:13px;font-weight:600}
.next{position:absolute;width:38px;height:38px;border-radius:50%;background:var(--white);box-shadow:0 2px 6px rgba(0,0,0,.2)}

/* portfolio */
.tile{position:absolute}
.rule{position:absolute;height:1px;background:#9a9a9a}
.arrow-btn{position:absolute;width:38px;height:38px;border-radius:50%;background:var(--red)}

/* testimonials */
.testimonials{left:0;top:3440px;width:1200px;height:701px;background:var(--gray)}
.card{position:absolute;top:3651px;width:337px;height:249px;background:var(--white);padding:38px 26px 0}
.card p{font-size:15.5px;line-height:25.5px;color:var(--text);text-align:justify;text-align-last:center}
.quote{position:absolute;top:3620px;width:337px;text-align:center;font-size:48px;font-weight:700;color:#333;line-height:1}
.avatar{position:absolute;top:3841px;width:120px;height:120px;border-radius:50%;background:radial-gradient(circle at 50% 45%,#8a8a8a,#3a3a3a)}
.person{position:absolute;top:3988px;width:337px;text-align:center}
.person strong{display:block;font-size:19px;font-weight:500;color:var(--ink)}
.person span{display:block;font-size:13.5px;color:var(--red);margin-top:4px}

/* footer */
.site-footer{left:0;top:4141px;width:1200px;height:382px;background:var(--black);color:var(--white)}
.site-footer .brand{left:0;width:1200px;justify-content:center;top:72px;font-size:36px;letter-spacing:8px}
.address{left:0;width:1200px;top:165px;text-align:center;font-size:15px;line-height:20px}
.contacts{left:0;width:1200px;top:226px;display:flex;justify-content:center;gap:60px;font-size:15px;align-items:center}
.contacts div{display:flex;align-items:center;gap:12px}
.contacts .ic{width:30px;height:30px;border-radius:50%;background:var(--red);display:flex;align-items:center;justify-content:center}
.footer-nav{left:0;width:1200px;top:301px;display:flex;justify-content:center;font-size:15px}
.footer-nav a{padding:0 28px;border-left:1px solid #777}
.footer-nav a:first-child{border-left:none}
.copybar{left:0;top:4523px;width:1200px;height:47px;background:var(--red);color:var(--white)}
.copybar p{position:absolute;left:88px;top:15px;font-size:13px}
.social{position:absolute;right:86px;top:12px;display:flex;gap:5px}
.social i{width:23px;height:23px;border-radius:50%;border:1.5px solid var(--white)}
</style>
</head>
<body>

<header class="site-header">
  <div class="brand"><span class="mark"></span>Vellmark Builders</div>
  <nav class="main-nav">
    <a class="active" href="#">Home</a><a href="#">About Us</a><a href="#">Services</a><a href="#">Portfolio</a><a href="#">Testimonials</a><a href="#">Contact Us</a>
  </nav>
</header>

<section class="hero">
  <div class="hero-photo" role="img" aria-label="Photo of a two-storey suburban home at dusk with warm lit windows"></div>
  <svg class="abs" style="left:0;top:0" width="1200" height="552" aria-hidden="true"><polygon points="0,0 690,0 355,552 0,552" fill="#ffffff" fill-opacity="0.62"/></svg>
  <h1>PRAESENT SUSCIPIT CONSE<br>CTETUR MAGNA A VEST</h1>
  <p>Lorem ipsum is placeholder text commonly used in the graphic, print, and publishing industries for previewing</p>
  <a class="btn" href="#">Read More</a>
  <div class="scroll-cue"><svg width="40" height="40" aria-hidden="true"><polyline points="13,17 20,24 27,17" fill="none" stroke="#e5353b" stroke-width="2.5"/></svg></div>
</section>

<section class="about">
  <div class="abs about-block"></div>
  <div class="abs about-frame"></div>
  <div class="abs about-img" role="img" aria-label="Photo of a bright white kitchen with steel refrigerator and pendant lamp"></div>
  <h2 class="abs section-title about-title">About <span>Us</span></h2>
  <p class="abs about-text">Lorem ipsum dolor sit amet, consectetur adipiscing elit, sed do eiusmod tempor incididunt ut labore et dolore magna aliqua. Ut enim ad minim veniam, quis nostrud exercitation ullamco laboris nisi ut aliquip ex ea commodo consequat. Duis aute irure dolor in reprehenderit in voluptate velit esse cillum</p>
  <a class="abs btn about-btn" href="#">Contact Us</a>
</section>

<section class="abs services">
  <h2 class="abs section-title center-title" style="top:122px">What <span>We Do ?</span></h2>

  <div class="service">
    <div class="abs band" style="top:225px;height:281px"></div>
    <div class="abs red-block" style="left:943px;top:185px;width:257px;height:358px"></div>
    <div class="abs frame" style="left:616px;top:215px;width:410px;height:300px;border-right:none;border-bottom:none"></div>
    <div class="abs kitchen" style="left:634px;top:227px;width:486px;height:279px" role="img" aria-label="Photo of a white kitchen with island and pendant lights"></div>
    <div class="next" style="left:874px;top:487px"><svg width="38" height="38" aria-hidden="true"><polyline points="16,12 23,19 16,26" fill="none" stroke="#e5353b" stroke-width="2.2"/></svg></div>
    <h3 style="left:85px;top:268px">Kitchen Designs</h3>
    <p style="left:85px;top:312px">Lorem ipsum dolor sit amet, slitconsectetur adipiscing elit. Nulla de sit ultricies efficitur orci nec sagittis nghevnfdhgbf consectetur adipiscing elit. Nulla de it ultricies efficitur orci nec sagittis sit ultricies efficitur orci nec sagi</p>
    <a class="btn" href="#" style="left:85px;top:433px">Read More</a>
  </div>

  <div class="service">
    <div class="abs band" style="top:568px;height:280px"></div>
    <div class="abs red-block" style="left:0;top:529px;width:259px;height:359px"></div>
    <div class="abs frame" style="left:160px;top:560px;width:408px;height:290px;border-left:none;border-bottom:none"></div>
    <div class="abs kitchen" style="left:83px;top:568px;width:476px;height:280px" role="img" aria-label="Photo of a white kitchen with island and pendant lights"></div>
    <div class="next" style="left:294px;top:829px"><svg width="38" height="38" aria-hidden="true"><polyline points="16,12 23,19 16,26" fill="none" stroke="#e5353b" stroke-width="2.2"/></svg></div>
    <h3 style="left:658px;top:611px">Bathroom Designs</h3>
    <p style="left:658px;top:655px">Lorem ipsum dolor sit amet, slitconsectetur adipiscing elit. Nulla de sit ultricies efficitur orci nec sagittis nghevnfdhgbf consectetur adipiscing elit. Nulla de it ultricies efficitur orci nec sagittis sit ultricies efficitur orci nec sagi</p>
    <a class="btn" href="#" style="left:660px;top:776px">Read More</a>
  </div>

  <div class="service">
    <div class="abs band" style="top:916px;height:279px"></div>
    <div class="abs red-block" style="left:943px;top:868px;width:257px;height:360px"></div>
    <div class="abs frame" style="left:616px;top:902px;width:410px;height:300px;border-right:none;border-bottom:none"></div>
    <div class="abs kitchen" style="left:630px;top:916px;width:487px;height:279px" role="img" aria-label="Photo of a white open-plan home interior with kitchen island"></div>
    <div class="next" style="left:874px;top:1176px"><svg width="38" height="38" aria-hidden="true"><polyline points="16,12 23,19 16,26" fill="none" stroke="#e5353b" stroke-width="2.2"/></svg></div>
    <h3 style="left:85px;top:957px">Home Designs</h3>
    <p style="left:85px;top:1001px">Lorem ipsum dolor sit amet, slitconsectetur adipiscing elit. Nulla de sit ultricies efficitur orci nec sagittis nghevnfdhgbf consectetur adipiscing elit. Nulla de it ultricies efficitur orci nec sagittis sit ultricies efficitur orci nec sagi</p>
    <a class="btn" href="#" style="left:85px;top:1123px">Read More</a>
  </div>
</section>

<section class="portfolio">
  <h2 class="abs section-title center-title" style="top:2772px">Our <span>Portfolio</span></h2>
  <div class="tile kitchen" style="left:85px;top:2884px;width:400px;height:210px" role="img" aria-label="Photo of a white kitchen"></div>
  <div class="tile" style="left:502px;top:2884px;width:268px;height:210px;background:linear-gradient(90deg,#8a5a2e,#c9a27a 40%,#e9e4dc 60%,#3a3532)" role="img" aria-label="Photo of a bathroom with freestanding tub and glass shower"></div>
  <div class="tile" style="left:788px;top:2884px;width:330px;height:210px;background:linear-gradient(180deg,#3f7fc6 0%,#8fb8e2 35%,#f2f2f2 55%,#2a7f8a 75%,#3d5a2a 100%)" role="img" aria-label="Photo of a modern white house under a blue sky"></div>
  <div class="tile" style="left:85px;top:3110px;width:330px;height:211px;background:linear-gradient(170deg,#9aa2bb,#6a6f86 45%,#c7a07a 70%,#4f6b3a)" role="img" aria-label="Photo of a suburban home at dusk"></div>
  <div class="tile" style="left:444px;top:3110px;width:257px;height:191px;background:linear-gradient(90deg,#2f3b2a,#b9824f 35%,#8b5a33 65%,#1d2636)" role="img" aria-label="Photo of a stone bathtub against wooden panelling"></div>
  <div class="tile" style="left:717px;top:3110px;width:401px;height:211px;background:linear-gradient(90deg,#e6e6e4,#c9c3b8 35%,#f4f4f2 60%,#d8dadc)" role="img" aria-label="Photo of a bright bathroom with round mirror and shower"></div>
  <div class="rule" style="left:85px;top:3376px;width:458px"></div>
  <div class="rule" style="left:664px;top:3376px;width:456px"></div>
  <div class="arrow-btn" style="left:558px;top:3357px"><svg width="38" height="38" aria-hidden="true"><polyline points="22,12 15,19 22,26" fill="none" stroke="#fff" stroke-width="2.2"/></svg></div>
  <div class="arrow-btn" style="left:609px;top:3357px"><svg width="38" height="38" aria-hidden="true"><polyline points="16,12 23,19 16,26" fill="none" stroke="#fff" stroke-width="2.2"/></svg></div>
</section>

<section class="abs testimonials">
  <h2 class="abs section-title center-title" style="top:88px;left:0">Client <span>Testimonials</span></h2>
</section>
<div class="card" style="left:222px"><p>Lorem ipsum dolor sit amet, consectetur adipiscing elit. Cras nec libero gravida lacus consectetur sagittis. Integer dapibus libero vel magna volutpat interdum.</p></div>
<div class="quote" style="left:222px">&ldquo;</div>
<div class="avatar" style="left:330px" role="img" aria-label="Portrait photo of a client"></div>
<div class="person" style="left:222px"><strong>LOREM IPSUM</strong><span>SIT AMET</span></div>
<div class="card" style="left:621px"><p>Lorem ipsum dolor sit amet, consectetur adipiscing elit. Cras nec libero gravida lacus consectetur sagittis. Integer dapibus libero vel magna volutpat interdum.</p></div>
<div class="quote" style="left:621px">&ldquo;</div>
<div class="avatar" style="left:727px" role="img" aria-label="Portrait photo of a client"></div>
<div class="person" style="left:621px"><strong>LOREM IPSUM</strong><span>SIT AMET</span></div>
<div class="rule" style="left:82px;top:4088px;width:456px"></div>
<div class="rule" style="left:662px;top:4088px;width:456px"></div>
<div class="arrow-btn" style="left:555px;top:4069px"><svg width="38" height="38" aria-hidden="true"><polyline points="22,12 15,19 22,26" fill="none" stroke="#fff" stroke-width="2.2"/></svg></div>
<div class="arrow-btn" style="left:606px;top:4069px"><svg width="38" height="38" aria-hidden="true"><polyline points="16,12 23,19 16,26" fill="none" stroke="#fff" stroke-width="2.2"/></svg></div>

<footer class="abs site-footer">
  <div class="brand"><span class="mark" style="width:40px;height:40px"></span>Vellmark Builders</div>
  <p class="abs address">Address line dummy here<br>Address line dummy, Country name</p>
  <div class="abs contacts">
    <div><span class="ic"><svg width="16" height="12" aria-hidden="true"><rect x="0.5" y="0.5" width="15" height="11" fill="none" stroke="#fff"/><polyline points="1,1 8,7 15,1" fill="none" stroke="#fff"/></svg></span>info@vellmarkbuilders.com</div>
    <div><span class="ic"><svg width="16" height="16" viewBox="0 0 24 24" aria-hidden="true"><path d="M6.6 10.8a15 15 0 006.6 6.6l2.2-2.2c.3-.3.7-.4 1-.2 1.1.4 2.3.6 3.6.6.6 0 1 .4 1 1V20c0 .6-.4 1-1 1A17 17 0 013 4c0-.6.4-1 1-1h3.5c.6 0 1 .4 1 1 0 1.3.2 2.5.6 3.6.1.3 0 .7-.2 1z" fill="#fff"/></svg></span>+1 209 555 0147</div>
  </div>
  <nav class="abs footer-nav"><a href="#">Home</a><a href="#">About Us</a><a href="#">Services</a><a href="#">Portfolio</a><a href="#">Testimonials</a><a href="#">Contact Us</a></nav>
</footer>
<div class="abs copybar">
  <p>Copyright © 2023 All Rights Reserved By Vellmark Builders</p>
  <div class="social"><i></i><i></i><i></i><i></i><i></i></div>
</div>

</body>
</html>
```